Trade Show Backdrop

I need a fun and unique design using our colors and verbiage. I have uploaded an example of what was already created and as you can see, it's lame.
I need it to say the same thing, but I want a bit more flare to the layout and graphics.
I have also uploaded what the competition uses.
I would like a clean look, no pictures. Obviously it has to be scale for a 10x10 booth, stand and

Target Market(s)

Private, Commercial and Public

Font styles to use
Sans Serif

Colors
fbed22
ffffff

Requirements
Must have
• Yellow, Gray, Black & WhiteAsphalt background- uploaded

```html
<!DOCTYPE html>
<html lang="en">
<head>
<meta charset="utf-8">
<title>The Road Maven – Trade Show Backdrop</title>
<link href="https://fonts.googleapis.com/css2?family=Barlow+Condensed:wght@600;700;800&display=swap" rel="stylesheet">
<style>
  :root {
    --asphalt: #3c3c3d;
    --asphalt-deep: #2b2b2c;
    --road-light: #2a2a2b;
    --road-dark: #1c1c1d;
    --gold: #e2bb3a;
    --ink: #2a2a2a;
    --white: #f2f2f2;
  }
  html, body { margin: 0; padding: 0; overflow: hidden; background: #e0ddda; }
  .backdrop {
    position: relative;
    width: 1200px; height: 908px;
    overflow: hidden;
    background: radial-gradient(ellipse at 70% 40%, var(--asphalt) 0%, var(--asphalt-deep) 100%);
    font-family: "Barlow Condensed", sans-serif;
    color: var(--white);
  }
  .shapes { position: absolute; inset: 0; }
  .brand-name {
    position: absolute; left: 476px; top: 200px; width: 240px;
    text-align: center; margin: 0;
    font-size: 46px; font-weight: 800; line-height: 0.95;
    color: var(--gold);
  }
  .solutions { position: absolute; left: 44px; top: 122px; }
  .solutions h2 {
    margin: 0 0 10px; font-size: 72px; font-weight: 800; color: var(--gold);
    line-height: 1; letter-spacing: 0.5px;
  }
  .solutions ul { list-style: none; margin: 0; padding: 0; }
  .solutions li {
    position: relative; padding-left: 26px;
    font-size: 42px; font-weight: 700; line-height: 47px;
  }
  .solutions li.bullet::before {
    content: ""; position: absolute; left: 0; top: 19px; width: 13px; height: 13px;
    border-radius: 50%; background: var(--gold);
  }
  .headline { position: absolute; right: 61px; top: 24px; text-align: right; color: var(--gold); }
  .headline .kicker { font-size: 44px; font-weight: 700; line-height: 1; }
  .headline .title {
    margin: 10px 0 0; font-size: 96px; font-weight: 800; line-height: 76px;
    letter-spacing: 0.5px;
  }
  .services-label {
    position: absolute; right: 61px; top: 272px; margin: 0;
    font-size: 80px; font-weight: 800; color: var(--ink); line-height: 1;
  }
  .services {
    position: absolute; right: 61px; top: 384px;
    list-style: none; margin: 0; padding: 0; text-align: right;
  }
  .services li {
    position: relative; padding-right: 44px;
    font-size: 54px; font-weight: 700; line-height: 66px;
  }
  .services li::after {
    content: ""; position: absolute; right: 0; top: 27px; width: 15px; height: 15px;
    border-radius: 50%; background: var(--gold);
  }
  .contact {
    position: absolute; left: 290px; top: 822px; width: 870px;
    display: flex; align-items: center; justify-content: center; gap: 9px;
    color: var(--ink); font-size: 54px; font-weight: 800; line-height: 1;
  }
  .social { width: 38px; height: 38px; border: 3px solid var(--ink); border-radius: 50%; box-sizing: border-box; }
  .url { margin: 0 10px; }
</style>
</head>
<body>
<main class="backdrop">
  <svg class="shapes" width="1200" height="908" viewBox="0 0 1200 908">
    <defs>
      <linearGradient id="roadTone" x1="0" y1="0" x2="1" y2="1">
        <stop offset="0" stop-color="var(--road-light)"/>
        <stop offset="1" stop-color="var(--road-dark)"/>
      </linearGradient>
    </defs>
    <polygon role="img" aria-label="Diagonal road illustration area"
      points="250,0 420,0 680,274 110,908 -60,908 -60,840 510,274"
      fill="url(#roadTone)"/>
    <polygon points="760,262 1200,262 1200,362 680,362" fill="var(--gold)" aria-hidden="true"/>
    <polygon points="200,798 1200,808 1200,908 110,908" fill="var(--gold)" aria-hidden="true"/>
  </svg>

  <p class="brand-name">The<br>Road<br>Maven</p>

  <section class="solutions">
    <h2>SOLUTIONS</h2>
    <ul>
      <li class="bullet">Professionally</li>
      <li>Managed</li>
      <li class="bullet">ADA Compliance</li>
      <li class="bullet">Site Evaluations</li>
      <li class="bullet">Project &amp; Asset</li>
      <li class="bullet">Management</li>
    </ul>
  </section>

  <header class="headline">
    <div class="kicker">Pavement Solutions</div>
    <h1 class="title">CUSTOM MADE<br>FOR YOU</h1>
  </header>

  <h2 class="services-label">SERVICES</h2>
  <ul class="services">
    <li>Sealcoating</li>
    <li>Concrete Curbs</li>
    <li>Asphalt Paving</li>
    <li>Pavement Repairs</li>
    <li>Concrete Sidewalks</li>
    <li>Pavement Maintenance</li>
  </ul>

  <footer class="contact">
    <span class="social"></span><span class="social"></span><span class="social"></span>
    <span class="url">www.RoadMaven.com</span>
    <span class="social"></span><span class="social"></span><span class="social"></span>
  </footer>
</main>
</body>
</html>
```